Postcard for dumpster rental business

We need an attractive post card to entice other businesses to use our dumpster rental service. This is a business to business situation.
Target Market(s)
Roofing, property restoration and remodeling contractors
Industry/Entity Type
Dumpster rentals
Font styles to use
Sans Serif
Colors
0054AA
0677BA
7BADD7
CADEEF
E8F1F8
Requirements
Must have
- 47tossbins.net Dumpster rental Easy online booking Logo Guaranteed On Time Delivery (as a badge or button?) QR Code Picture of our dumpster (see website)
Nice to have
- Call to action "Order now!"

```html
<!DOCTYPE html>
<html lang="en">
<head>
<meta charset="utf-8">
<title>47toss Dumpster Rental – Postcard</title>
<link rel="stylesheet" href="https://fonts.googleapis.com/css2?family=Montserrat:wght@500;600;700;800;900&display=swap">
<style>
  :root {
    --stage: #606268;
    --paper: #ffffff;
    --navy: #1c2c5c;
    --blue: #1f74bb;
    --blue-deep: #0054aa;
    --blue-mid: #0677ba;
    --blue-light: #7badd7;
    --orange: #e8621f;
    --silver: #d6dae0;
    --ink: #1c2c5c;
  }
  * { box-sizing: border-box; margin: 0; padding: 0; }
  html, body {
    width: 1200px; height: 1200px; overflow: hidden;
    background: var(--stage);
    font-family: "Montserrat", Arial, sans-serif;
  }
  .postcard {
    position: absolute;
    width: 675px; height: 437px;
    background: var(--paper);
    overflow: hidden;
    transform: scale(1.2252);
    transform-origin: 0 0;
    box-shadow: 0 2px 6px rgba(0,0,0,.25);
  }
  .postcard--front { left: 180px; top: 53px; }
  .postcard--back  { left: 180px; top: 618px; }
  .shapes { position: absolute; inset: 0; width: 675px; height: 437px; }

  .brand { position: absolute; width: 200px; display: flex; flex-direction: column; align-items: center; }
  .brand__row { display: flex; align-items: center; gap: 8px; }
  .brand__mark { width: 22px; height: 22px; background: var(--blue); flex: none; }
  .brand__name {
    font-weight: 800; font-size: 16px; color: var(--blue);
    line-height: 1.05; text-transform: uppercase; text-align: center; white-space: nowrap;
  }
  .brand__phone { margin-top: 5px; font-size: 10.5px; font-weight: 700; color: var(--ink); letter-spacing: 1px; }

  .front-brand { left: 18px; top: 22px; }
  .back-brand  { left: 318px; top: 30px; }

  .headline { position: absolute; left: 30px; width: 380px; text-align: center; font-weight: 800; line-height: 1.08; }
  .headline--light { top: 205px; font-size: 23px; color: var(--silver); }
  .headline--accent { top: 230px; font-size: 23px; color: var(--orange); }
  .about {
    position: absolute; left: 38px; top: 291px; width: 365px;
    text-align: center; color: #fff; font-size: 11px; font-weight: 500; line-height: 1.27;
  }
  .web-button {
    position: absolute; left: 70px; top: 375px; width: 300px; height: 40px;
    background: var(--blue); display: flex; align-items: center; gap: 12px; padding-left: 10px;
  }
  .web-button__icon { width: 30px; height: 30px; background: #fff; display: flex; align-items: center; justify-content: center; }
  .web-button__text { color: #fff; font-weight: 800; font-size: 21px; }
  .booking {
    position: absolute; right: 14px; top: 383px; text-align: center;
    color: #fff; font-weight: 800; font-size: 11.5px; line-height: 1.1;
  }

  .guarantee { position: absolute; left: 17px; top: 133px; font-weight: 900; font-size: 20.5px; line-height: 1.15; }
  .guarantee__top { color: var(--silver); }
  .guarantee__bottom { color: var(--orange); }
  .takes-bar {
    position: absolute; left: 0; top: 183px; width: 268px; height: 22px;
    background: var(--orange); color: #fff; font-weight: 800; font-size: 11.5px;
    display: flex; align-items: center; padding-left: 17px;
  }
  .services {
    position: absolute; left: 17px; top: 216px; width: 330px;
    color: #fff; font-size: 11.3px; font-weight: 600; line-height: 1.27;
  }
  .services .dot { color: var(--orange); }
  .phone-box {
    position: absolute; left: 15px; top: 322px; width: 300px; height: 40px;
    background: #fff; display: flex; align-items: center; gap: 10px; padding-left: 10px;
  }
  .phone-box__icon { width: 28px; height: 28px; background: #8a8d93; display: flex; align-items: center; justify-content: center; }
  .phone-box__text { color: var(--blue-deep); font-weight: 800; font-size: 27px; }
  .stamp { position: absolute; left: 566px; top: 10px; width: 98px; height: 97px; border: 1px solid #9a9ea5; }
</style>
</head>
<body>

<section class="postcard postcard--front" aria-label="Postcard front">
  <svg class="shapes" viewBox="0 0 675 437">
    <defs>
      <linearGradient id="photoTone" x1="0" y1="0" x2="1" y2="1">
        <stop offset="0" stop-color="#2f7fc4"/>
        <stop offset=".55" stop-color="#1d5fa8"/>
        <stop offset="1" stop-color="#c9662a"/>
      </linearGradient>
    </defs>
    <polygon points="0,150 58,150 84,176 84,200 42,245 0,245" fill="var(--blue)"/>
    <polygon role="img" aria-label="Photo: worker loading scrap into orange roll-off dumpsters"
      points="240,8 667,8 667,188 525,325 470,325 240,85"
      fill="url(#photoTone)" stroke="url(#photoTone)" stroke-width="16" stroke-linejoin="round"/>
    <polygon points="0,437 0,272 148,118 236,118 410,292 410,437" fill="var(--navy)"
      stroke="var(--navy)" stroke-width="20" stroke-linejoin="round"/>
    <polygon points="560,437 675,312 675,437" fill="var(--blue)"/>
    <line x1="296" y1="146" x2="492" y2="366" stroke="var(--orange)" stroke-width="16" stroke-linecap="round"/>
    <g transform="translate(580 300) rotate(-50)">
      <rect x="-125" y="-27" width="260" height="54" fill="var(--orange)"/>
      <text x="0" y="12" text-anchor="middle" fill="#fff" font-family="Montserrat, Arial, sans-serif"
        font-weight="900" font-size="32">ORDER NOW!</text>
    </g>
  </svg>

  <div class="brand front-brand">
    <div class="brand__row"><span class="brand__mark"></span><span class="brand__name">47toss<br>Dumpster Rental</span></div>
    <div class="brand__phone">(555) 204-4718</div>
  </div>

  <h1 class="headline headline--light">DUMPSTER</h1>
  <h2 class="headline headline--accent">RENTAL AND<br>REMOVAL SERVICES</h2>
  <p class="about">47toss Dumpster Rental is locally owned and operated by a small-business team with a reputation that spans over 30 years. Our competitive prices &amp; high standards allow us to offer comprehensive, professional, and personalized customer-service to meet your practical and financial needs.</p>

  <div class="web-button">
    <span class="web-button__icon">
      <svg width="20" height="20" viewBox="0 0 20 20" fill="none" stroke="#6b6e74" stroke-width="1.6">
        <circle cx="10" cy="10" r="8"/><ellipse cx="10" cy="10" rx="3.5" ry="8"/><line x1="2" y1="10" x2="18" y2="10"/>
      </svg>
    </span>
    <span class="web-button__text">47tossbins.net</span>
  </div>

  <p class="booking">EASY<br>ONLINE<br>BOOKING</p>
</section>

<section class="postcard postcard--back" aria-label="Postcard back">
  <svg class="shapes" viewBox="0 0 675 437">
    <polygon points="0,190 300,190 425,315 425,372 0,372" fill="var(--blue)"/>
    <polygon points="0,100 88,12 142,12 320,190 0,190" fill="var(--navy)"
      stroke="var(--navy)" stroke-width="12" stroke-linejoin="round"/>
    <polyline points="156,14 442,300 442,366" fill="none" stroke="var(--orange)" stroke-width="16"
      stroke-linejoin="round" stroke-linecap="round"/>
    <rect role="img" aria-label="Photo: orange roll-off dumpster" x="45" y="75" width="80" height="48" fill="#e27a2c"/>
  </svg>

  <div class="brand back-brand">
    <div class="brand__row"><span class="brand__mark"></span><span class="brand__name">47toss<br>Dumpster Rental</span></div>
    <div class="brand__phone">(555) 204-4718</div>
  </div>
  <div class="stamp"></div>

  <h2 class="guarantee"><span class="guarantee__top">GUARANTEED</span><br><span class="guarantee__bottom">ON TIME DELIVERY</span></h2>
  <div class="takes-bar">WE TAKE JUST ABOUT EVERYTHING!</div>
  <p class="services">
    Refrigerator Disposal <span class="dot">•</span> Garbage Removal <span class="dot">•</span>
    Mattress Disposal <span class="dot">•</span> Foreclosure Clean Outs <span class="dot">•</span>
    Construction Waste Removal <span class="dot">•</span> Yard Waste Removal <span class="dot">•</span>
    Trash Removal <span class="dot">•</span> Appliance Removal <span class="dot">•</span>
    Television Disposal &amp; Recycling <span class="dot">•</span> Furniture Removal <span class="dot">•</span>
    E-Waste Disposal <span class="dot">•</span> Hot Tub Disposal
  </p>
  <div class="phone-box">
    <span class="phone-box__icon">
      <svg width="18" height="18" viewBox="0 0 24 24" fill="#fff">
        <path d="M6.6 10.8a15.1 15.1 0 0 0 6.6 6.6l2.2-2.2a1 1 0 0 1 1-.25 11.4 11.4 0 0 0 3.6.6 1 1 0 0 1 1 1V20a1 1 0 0 1-1 1A17 17 0 0 1 3 4a1 1 0 0 1 1-1h3.5a1 1 0 0 1 1 1c0 1.25.2 2.45.6 3.6a1 1 0 0 1-.25 1z"/>
      </svg>
    </span>
    <span class="phone-box__text">(555) 204-4718</span>
  </div>
</section>

</body>
</html>
```